parts and kits

we need an updated flyer to email to our customers
we need to have what we sell at kivo
caliper pistons
seal kits
new brake cylinders
brake boosters
brake shoes
brake pads
brake hoses
cables -accelerator, clutch, hand brake etc
for both private, vintage and commercial vehicles

```html
<!DOCTYPE html>
<html lang="en">
<head>
<meta charset="utf-8">
<title>Kivo Auto Centre – Parts and Kits</title>
<link rel="stylesheet" href="https://fonts.googleapis.com/css2?family=Montserrat:ital,wght@0,800;0,900;1,700;1,800&family=Roboto:ital,wght@1,500&family=Roboto+Condensed:wght@700&display=swap">
<style>
  :root {
    --yellow: #ffd900;
    --ink: #0d0d0d;
    --dark-1: #2b2c2e;
    --dark-2: #4a4b4d;
    --white: #ffffff;
    --photo-1: #e9ebee;
    --photo-2: #8d9198;
  }
  * { margin: 0; padding: 0; box-sizing: border-box; }
  html, body { width: 848px; height: 1200px; overflow: hidden; }
  body { font-family: "Montserrat", sans-serif; background: var(--dark-1); }

  .flyer {
    position: relative;
    width: 848px;
    height: 1200px;
    overflow: hidden;
    background:
      radial-gradient(ellipse 320px 700px at 150px 300px, rgba(255,255,255,0.12), transparent 70%),
      linear-gradient(160deg, var(--dark-2) 0%, var(--dark-1) 45%, #1c1d1f 100%);
  }
  .flyer__sweep { position: absolute; inset: 0; }

  .brand-box {
    position: absolute;
    left: 37px; top: 0;
    width: 270px; height: 191px;
    background: var(--yellow);
    display: flex; align-items: center; justify-content: center; gap: 8px;
  }
  .brand-box__mark { width: 16px; height: 16px; background: var(--ink); flex: none; }
  .brand-box__name { font-weight: 900; font-size: 19px; color: var(--ink); white-space: nowrap; }

  .product {
    position: absolute;
    width: 236px; height: 236px;
    border-radius: 50%;
    border: 5px solid var(--yellow);
    background: var(--white);
    overflow: hidden;
  }
  .product__photo {
    position: absolute; inset: 30px;
    border-radius: 50%;
    background: radial-gradient(circle at 45% 40%, var(--photo-1), var(--photo-2) 85%);
    opacity: 0.75;
  }
  .product--pads    { left: 488px; top: 110px; }
  .product--piston  { left: 304px; top: 283px; }
  .product--booster { left: 159px; top: 479px; }
  .product--shoes   { left: 19px;  top: 699px; }

  .master-cylinder {
    position: absolute;
    left: 549px; top: 376px;
    width: 262px; height: 208px;
    border-radius: 40px;
    background: radial-gradient(ellipse at 55% 40%, #b9b5a4, #3a3b3d 75%);
    opacity: 0.8;
  }

  .headline {
    position: absolute;
    right: 22px; top: 602px;
    font-weight: 900; font-size: 98px; line-height: 1;
    color: var(--ink); letter-spacing: -1px;
  }
  .headline-band {
    position: absolute;
    left: 391px; top: 704px;
    width: 457px; height: 54px;
    background: var(--ink);
    clip-path: polygon(30px 0, 100% 0, 100% 100%, 0 100%);
  }
  .headline-band__text {
    position: absolute;
    right: 24px; top: 0;
    font-weight: 900; font-size: 49px; line-height: 54px;
    color: var(--yellow);
    white-space: nowrap;
  }

  .tagline {
    position: absolute;
    right: 28px; top: 762px;
    text-align: right;
    font-family: "Roboto", sans-serif;
    font-style: italic; font-weight: 500;
    font-size: 31px; line-height: 39px;
    color: var(--ink);
  }

  .sell-band {
    position: absolute;
    left: 555px; top: 878px;
    width: 293px; height: 54px;
    background: var(--ink);
    clip-path: polygon(26px 0, 100% 0, 100% 100%, 0 100%);
  }
  .sell-band__text {
    position: absolute; right: 18px; top: 0;
    font-style: italic; font-weight: 800;
    font-size: 22px; line-height: 54px;
    color: var(--white);
    white-space: nowrap;
  }

  .range {
    position: absolute;
    left: 158px; top: 939px;
    width: 690px; height: 183px;
  }
  .range::before {
    content: "";
    position: absolute; inset: 0;
    background: var(--yellow);
    border-radius: 12px 0 0 12px;
    clip-path: polygon(51px 0, 100% 0, 100% 100%, 0 100%);
  }
  .range__list {
    list-style: none;
    position: absolute; right: 33px; top: 18px;
    text-align: right;
    font-style: italic; font-weight: 700;
    font-size: 21px; line-height: 36px;
    color: var(--ink);
    letter-spacing: -0.4px;
    white-space: nowrap;
  }

  .promise {
    position: absolute;
    left: 0; bottom: 0;
    width: 848px; height: 53px;
    background: var(--ink);
    font-family: "Roboto Condensed", sans-serif;
    font-weight: 700; font-size: 28px; line-height: 53px;
    color: var(--yellow);
    padding-left: 15px;
    white-space: nowrap;
  }
</style>
</head>
<body>
<main class="flyer">
  <svg class="flyer__sweep" width="848" height="1200" viewBox="0 0 848 1200" aria-hidden="true">
    <path d="M848 0 Q250 380 0 1170 L0 1200 L848 1200 Z" fill="#ffffff"/>
  </svg>

  <div class="brand-box">
    <span class="brand-box__mark"></span>
    <span class="brand-box__name">KIVO AUTO CENTRE</span>
  </div>

  <div class="product product--pads"><div class="product__photo" role="img" aria-label="Photo of a pair of brake pads"></div></div>
  <div class="product product--piston"><div class="product__photo" role="img" aria-label="Photo of a caliper piston"></div></div>
  <div class="product product--booster"><div class="product__photo" role="img" aria-label="Photo of a brake booster with master cylinder"></div></div>
  <div class="product product--shoes"><div class="product__photo" role="img" aria-label="Photo of a pair of brake shoes"></div></div>
  <div class="master-cylinder" role="img" aria-label="Photo of a brake master cylinder"></div>

  <h1 class="headline">KIVO</h1>
  <div class="headline-band"><span class="headline-band__text">AUTO CENTRE</span></div>

  <p class="tagline">Specialise in the re-manufacture<br>of brakes, horses, and cable</p>

  <div class="sell-band"><span class="sell-band__text">WE SELL AT KIVO :</span></div>

  <div class="range">
    <ul class="range__list">
      <li>Caliper pistons, Seal kits, New Brake Cylinders</li>
      <li>Brake boosters, Brake Shoes Brake Pads, Brake hoses</li>
      <li>Cables -Accelerator, Clutch, Hand Brake etc</li>
      <li>For both Private, Vintage and Commercial Vehicles</li>
    </ul>
  </div>

  <p class="promise">Our aim is to repair parts with the quickest turn-around times possible.</p>
</main>
</body>
</html>
```